Label Design for a New Alcoholized Root Beer

Create a design for a new alcoholized root beer. This is a new product category in the USA growing very rapidly. Root Beer is a popular flavor of Cola, but recently, beer manufacturers have added alcohol to it and have created a new product that has gained traction on the market at a tremendous rate.

Root Beer is vintage product that has been around for a hundred years. Consumers of this product are mostly male between the age of 30 to 45. They purchase this product for its nostalgia and vintage look and taste.

This product will be in a standard 355 mL brown bottle.

It is 5.9% abv.

The name of the product is ''Corvel's Hard Root Beer''.

We have uploaded some pictures of traditional root beers to give you an idea of the feel we want our product to have and also, the bottle the product will be filled in.

Target Market(s)

Consumers are male 30-45, same market as craft beer consumers

Industry/Entity Type

Product

Requirements
Must have
• Design must have a vintage feel to it

```html
<!DOCTYPE html>
<html lang="en">
<head>
<meta charset="utf-8">
<title>Corvel's Hard Root Beer – Label</title>
<link href="https://fonts.googleapis.com/css2?family=Rye&display=swap" rel="stylesheet">
<style>
  :root {
    --paper: #ffffff;
    --ink: #1d1a16;
    --gold-light: #fbeec0;
    --gold: #e9c873;
    --gold-deep: #b8893a;
    --bronze: #6b4a1e;
    --red: #e8000b;
    --red-deep: #8e0a0a;
    --cream: #f7d9a2;
    --star-red: #e3141b;
    --star-maroon: #7a0d0d;
  }
  html, body {
    margin: 0;
    padding: 0;
    width: 1200px;
    height: 1023px;
    overflow: hidden;
    background: var(--paper);
  }
  .label {
    display: block;
    width: 1200px;
    height: 1023px;
  }
  .band-text {
    font-family: "Rye", serif;
    fill: var(--cream);
    letter-spacing: 6px;
  }
  .brand-name {
    font-family: "Rye", serif;
    fill: var(--ink);
    font-size: 64px;
    letter-spacing: 1px;
  }
</style>
</head>
<body>
<svg class="label" viewBox="0 0 1140 972" preserveAspectRatio="none" xmlns="http://www.w3.org/2000/svg">
  <defs>
    <radialGradient id="goldDisc" cx="50%" cy="45%" r="60%">
      <stop offset="0" stop-color="var(--gold-light)"/>
      <stop offset="0.6" stop-color="var(--gold)"/>
      <stop offset="1" stop-color="var(--gold-deep)"/>
    </radialGradient>
    <linearGradient id="redBand" x1="0" x2="1" y1="0" y2="0">
      <stop offset="0" stop-color="var(--red)"/>
      <stop offset="0.7" stop-color="var(--red)"/>
      <stop offset="1" stop-color="var(--red-deep)"/>
    </linearGradient>
    <radialGradient id="medallionFill" cx="50%" cy="50%" r="50%">
      <stop offset="0" stop-color="#c9a35a"/>
      <stop offset="0.7" stop-color="#8a6a34"/>
      <stop offset="1" stop-color="#3a2c18"/>
    </radialGradient>
    <linearGradient id="scrollFill" x1="0" x2="0" y1="0" y2="1">
      <stop offset="0" stop-color="var(--gold-light)"/>
      <stop offset="0.5" stop-color="#c9a05a"/>
      <stop offset="1" stop-color="var(--gold-light)"/>
    </linearGradient>
    <linearGradient id="barFill" x1="0" x2="1">
      <stop offset="0" stop-color="var(--gold-light)"/>
      <stop offset="0.5" stop-color="var(--gold)"/>
      <stop offset="1" stop-color="var(--gold-light)"/>
    </linearGradient>
    <path id="arcTop" d="M 295 485 A 275 275 0 0 1 845 485"/>
    <path id="arcBottom" d="M 262 485 A 308 308 0 0 0 878 485"/>
  </defs>

  <!-- disc -->
  <circle class="disc-rim" cx="570" cy="485" r="392" fill="var(--ink)"/>
  <circle class="disc" cx="570" cy="485" r="384" fill="url(#goldDisc)"/>
  <circle class="disc-line" cx="570" cy="485" r="350" fill="none" stroke="var(--bronze)" stroke-width="2"/>

  <!-- red bands -->
  <path class="band band-top" d="M 271 345 A 330 330 0 0 1 869 345 L 777 345 A 250 250 0 0 0 363 345 Z"
        fill="url(#redBand)" stroke="var(--red-deep)" stroke-width="3"/>
  <path class="band band-bottom" d="M 271 625 A 330 330 0 0 0 869 625 L 777 625 A 250 250 0 0 1 363 625 Z"
        fill="url(#redBand)" stroke="var(--red-deep)" stroke-width="3"/>

  <!-- central medallion -->
  <circle class="medallion" cx="570" cy="485" r="238" fill="url(#medallionFill)"
          role="img" aria-label="Engraved gold filigree medallion"/>

  <!-- side scrolls -->
  <rect class="side-scroll side-scroll-left" x="112" y="318" width="140" height="348" rx="60"
        fill="url(#scrollFill)" stroke="var(--bronze)" stroke-width="2"
        role="img" aria-label="Engraved gold scrollwork"/>
  <rect class="side-scroll side-scroll-right" x="888" y="318" width="140" height="348" rx="60"
        fill="url(#scrollFill)" stroke="var(--bronze)" stroke-width="2"
        role="img" aria-label="Engraved gold scrollwork"/>

  <!-- horizontal frame bars -->
  <rect class="frame-bar" x="240" y="388" width="660" height="208" fill="url(#barFill)" stroke="var(--ink)" stroke-width="3"/>
  <rect class="frame-bar-inner" x="256" y="402" width="628" height="180" fill="none" stroke="var(--ink)" stroke-width="2"/>

  <!-- side diamonds -->
  <path class="diamond" d="M 130 490 L 146 476 L 162 490 L 146 504 Z" fill="var(--red)" stroke="var(--ink)" stroke-width="2"/>
  <path class="diamond" d="M 978 490 L 994 476 L 1010 490 L 994 504 Z" fill="var(--red)" stroke="var(--ink)" stroke-width="2"/>

  <!-- name banner -->
  <rect class="banner-outer" x="188" y="424" width="764" height="126" rx="60" fill="var(--ink)"/>
  <rect class="banner" x="196" y="432" width="748" height="110" rx="54" fill="var(--paper)"/>
  <rect class="banner-line" x="206" y="442" width="728" height="90" rx="45" fill="none" stroke="var(--ink)" stroke-width="2"/>

  <polygon class="star star-left"
    points="258,466 264,482 281,482 267,492 272,509 258,499 244,509 249,492 235,482 252,482"
    fill="var(--star-red)"/>
  <polygon class="star star-right"
    points="882,466 888,482 905,482 891,492 896,509 882,499 868,509 873,492 859,482 876,482"
    fill="var(--star-maroon)"/>

  <text class="brand-name" x="570" y="512" text-anchor="middle">Corvel's Hard</text>

  <!-- band text -->
  <text class="band-text" font-size="40">
    <textPath href="#arcTop" startOffset="50%" text-anchor="middle">ROOT BEER</textPath>
  </text>
  <text class="band-text" font-size="36">
    <textPath href="#arcBottom" startOffset="50%" text-anchor="middle">5.9% ALC / VOL</textPath>
  </text>
</svg>
</body>
</html>
```